We need an attractive business card design that is modern and inviting. We like the blue and yellow (or gold) colors that are displayed with the logo. The business should communicate trust, experience, and integrity.

Target Market(s)

Residential and Commercial

Industry/Entity Type

Business

Contact Information for Business Card

Recessed Lighting
LED Retro Fit
Sign Repair
Alarms and Cameras
Mobile Home Services
24hr service calls

Font styles to use
Serif
Sans Serif

Colors
3176b5
0455a3
fece3e
fbee3e

Requirements
Must have
• Brannick Electric
• Owner: Marcus Brannick
• Licensed and Insured
• TECL #58731
Nice to have
• Exquisite Detail!!
• Over 20 years of experience
Should not have
• Nothing boring or traditional!!!

```html
<!DOCTYPE html>
<html lang="en">
<head>
<meta charset="utf-8">
<title>Brannick Electric – Business Card</title>
<link rel="stylesheet" href="https://fonts.googleapis.com/css2?family=Arimo:wght@400;700&display=swap">
<style>
  :root {
    --blue-deep: #0455a3;
    --blue-mid: #1a5fae;
    --blue-light: #3176b5;
    --yellow: #fece3e;
    --yellow-bright: #fbee3e;
    --yellow-card: #e6d92e;
    --white: #ffffff;
    --owner-grey: #dfe6ef;
    --stage: #333538;
  }
  * { box-sizing: border-box; margin: 0; padding: 0; }
  html, body {
    width: 1200px;
    height: 997px;
    overflow: hidden;
    background: var(--stage);
    font-family: "Arimo", Arial, sans-serif;
  }
  .sheet {
    width: 1200px;
    height: 997px;
    display: flex;
    flex-direction: column;
    align-items: center;
    justify-content: center;
    gap: 56px;
  }
  .card {
    position: relative;
    width: 700px;
    height: 400px;
    border-radius: 22px;
    overflow: hidden;
    box-shadow: 0 14px 34px rgba(0,0,0,.45);
  }
  .card-bg { position: absolute; inset: 0; width: 100%; height: 100%; }

  /* brand lockup */
  .brand {
    position: absolute;
    display: flex;
    flex-direction: column;
    align-items: flex-start;
    gap: 10px;
  }
  .brand-dot {
    width: 40px; height: 40px;
    border-radius: 50%;
    border: 5px solid var(--blue-deep);
  }
  .brand-name {
    font-weight: 700;
    font-size: 32px;
    letter-spacing: 1.5px;
    color: var(--blue-deep);
    line-height: 1.05;
    text-transform: uppercase;
  }
  .card-back .brand { left: 62px; top: 190px; }
  .card-front .brand { left: 62px; top: 100px; }

  /* services list */
  .services {
    position: absolute;
    right: 36px;
    top: 34px;
    list-style: none;
    color: var(--yellow-bright);
  }
  .services-title {
    font-size: 13px;
    letter-spacing: 1px;
    text-align: right;
    padding-right: 28px;
    margin-bottom: 12px;
  }
  .service {
    display: flex;
    justify-content: flex-end;
    align-items: center;
    gap: 10px;
    font-size: 16px;
    line-height: 1;
    margin-bottom: 11px;
  }
  .tick-box {
    width: 18px; height: 18px;
    border: 1.5px solid var(--yellow-bright);
    border-radius: 3px;
    flex: none;
  }
  .tick-spacer { width: 18px; height: 18px; flex: none; }

  /* front: owner + credentials */
  .owner {
    position: absolute;
    right: 40px; top: 38px;
    text-align: right;
  }
  .owner-name {
    font-weight: 700;
    font-size: 26px;
    color: var(--yellow-bright);
  }
  .owner-role {
    font-weight: 700;
    font-size: 15px;
    color: var(--owner-grey);
    margin-top: 4px;
  }
  .credentials {
    position: absolute;
    left: 62px; top: 290px;
    font-weight: 700;
    font-size: 21px;
    line-height: 1.3;
    color: var(--blue-deep);
    text-align: center;
  }
  .contacts {
    position: absolute;
    right: 40px; top: 232px;
    list-style: none;
    color: var(--white);
  }
  .contact {
    display: flex;
    justify-content: flex-end;
    align-items: center;
    gap: 12px;
    font-size: 17px;
    margin-bottom: 20px;
  }
  .contact-icon {
    width: 24px; height: 24px;
    border-radius: 5px;
    background: var(--yellow-card);
    display: flex; align-items: center; justify-content: center;
    flex: none;
  }
  .contact-icon svg { width: 14px; height: 14px; }
</style>
</head>
<body>
<main class="sheet">

  <!-- back side: services -->
  <section class="card card-back">
    <svg class="card-bg" viewBox="0 0 700 400" aria-hidden="true">
      <rect width="700" height="400" fill="var(--blue-mid)"/>
      <circle cx="40" cy="420" r="392" fill="var(--yellow-card)"/>
      <circle cx="20" cy="420" r="380" fill="var(--white)"/>
    </svg>
    <div class="brand">
      <span class="brand-dot"></span>
      <span class="brand-name">Brannick<br>Electric</span>
    </div>
    <ul class="services">
      <li class="services-title">OUR SERVICES</li>
      <li class="service">Sign Repair <svg class="tick-box" viewBox="0 0 18 18"><path d="M4 9l3 3 7-7" fill="none" stroke="var(--yellow-bright)" stroke-width="2"/></svg></li>
      <li class="service">LED Retro Fit <svg class="tick-box" viewBox="0 0 18 18"><path d="M4 9l3 3 7-7" fill="none" stroke="var(--yellow-bright)" stroke-width="2"/></svg></li>
      <li class="service">24hr service calls <svg class="tick-box" viewBox="0 0 18 18"><path d="M4 9l3 3 7-7" fill="none" stroke="var(--yellow-bright)" stroke-width="2"/></svg></li>
      <li class="service">Recessed Lighting <svg class="tick-box" viewBox="0 0 18 18"><path d="M4 9l3 3 7-7" fill="none" stroke="var(--yellow-bright)" stroke-width="2"/></svg></li>
      <li class="service">Alarms and Cameras <svg class="tick-box" viewBox="0 0 18 18"><path d="M4 9l3 3 7-7" fill="none" stroke="var(--yellow-bright)" stroke-width="2"/></svg></li>
      <li class="service">Mobile Home Services <svg class="tick-box" viewBox="0 0 18 18"><path d="M4 9l3 3 7-7" fill="none" stroke="var(--yellow-bright)" stroke-width="2"/></svg></li>
      <li class="service">Residential &amp; Commercial <span class="tick-spacer"></span></li>
    </ul>
  </section>

  <!-- front side: owner & contact -->
  <section class="card card-front">
    <svg class="card-bg" viewBox="0 0 700 400" aria-hidden="true">
      <rect width="700" height="400" fill="var(--blue-mid)"/>
      <circle cx="35" cy="200" r="410" fill="var(--yellow-card)"/>
      <circle cx="20" cy="200" r="400" fill="var(--white)"/>
    </svg>
    <div class="owner">
      <p class="owner-name">Marcus Brannick</p>
      <p class="owner-role">Owner</p>
    </div>
    <div class="brand">
      <span class="brand-dot"></span>
      <span class="brand-name">Brannick<br>Electric</span>
    </div>
    <p class="credentials">Licensed &amp; Insured<br>TECL #58731</p>
    <ul class="contacts">
      <li class="contact">512-476-2190
        <span class="contact-icon"><svg viewBox="0 0 14 14"><rect x="3.5" y="1" width="7" height="12" rx="1.5" fill="none" stroke="var(--blue-deep)" stroke-width="1.6"/></svg></span>
      </li>
      <li class="contact">mb@brannick.com
        <span class="contact-icon"><svg viewBox="0 0 14 14"><rect x="1" y="3" width="12" height="8" fill="none" stroke="var(--blue-deep)" stroke-width="1.5"/><path d="M1 3l6 5 6-5" fill="none" stroke="var(--blue-deep)" stroke-width="1.5"/></svg></span>
      </li>
      <li class="contact">brannickelectric.com
        <span class="contact-icon"><svg viewBox="0 0 14 14"><rect x="1" y="5" width="7" height="4" rx="2" transform="rotate(-45 4.5 7)" fill="none" stroke="var(--blue-deep)" stroke-width="1.5"/><rect x="6" y="5" width="7" height="4" rx="2" transform="rotate(-45 9.5 7)" fill="none" stroke="var(--blue-deep)" stroke-width="1.5"/></svg></span>
      </li>
    </ul>
  </section>

</main>
</body>
</html>
```